Tourism Marketing needing sleek, clear design for business card & proposal documents.

***Company background***
"Quiet Harbour" is a company specializing in tourism marketing and project management. We do international wholesale, event management as well as ongoing representation of tourism and hospitality companies.

***Target market***
We cater to tourism companies and hotel professionals.

***Task***
We would like to get a single sided business card designed (but will still consider two sided, we are open to any ideas you may have). The layout for this card should be modern and elegant. Currently we do not have a logo, but we would like our business name in a really simple typography for the business card (similar to Moonrise Palace's logo - www.moonrisepalace-example.com.au).We are after a design that is clear, strong enough to be recognised as Quiet Harbour that does not require any fancy design. Another option is a simple play on QH (Quiet Harbour) or simply have Quiet Harbour featured elsewhere on card more as a brand/logo.

Feel free to submit different fonts if you feel you have any other fonts/designs that may be suitable for this card other than sans serifs. Should this project be successful, we will be considering several other projects for business proposal templates and eventually a website design.

The information that needs to go on the card are as follows:

Marta Holloway
Director
Quiet Harbour
Tourism Marketing & Representation
87 Wendover Parade
Prahran, Victoria, 3181 Australia
T +61 498203617 E marta@quietharbour-example.com.au

***Look and feel***
We'd like the business card design to express the following:
Modern, sleek, elegant, simple, discreet, quality, subtle, professional, creative, innovation

In terms of typography, we like something really simple and blocky (similar font to Moonrise Palace's logo - www.moonrisepalace-example.com.au)

***Colour scheme***
Shades of grey and dark teal

***Note***
Although our main target market are professionals, we would like the business card design to be versatile enough to be used outside of the tourism industry and need to appeal to different markets.

I do not have existing logo. Was hoping for a design that may be clear, strong enough not to require one. Other option is a simple play on QH (Quiet Harbour) or simply have Quiet Harbour featured elsewhere on card more as a brand/logo.

Marta Holloway
Director
Quiet Harbour Pty Ltd 
87 Wendover Parade
T +61 498203617  E  marta@quietharbour-example.com.au

Thank you for designs so far. Many have used a mauve colour which matches our company profile. This is not necessary, as that is just a draft and will be completely redesigned, so dont  feel you need to incorporate the mauve.

My colour preferences are for a white or grey background, and I like fonts in dark teals, grey or other sophisticated but modern colours. feel free to submit different fonts if you you have other fonts you thing would be suitable for this card, along with sans serifs. Should this project be successful, we will be considering several others for business proposal templates and eventually website. 

Target Market(s)

International Hospitality Senior Executives, Directors of International Tourism Companies, Directors of Tourism Bodies Internationally, local Tourism

Industry/Entity Type

Hospitality

Requirements
Should not have
• must not have bright garish colour, swirly patterns or anything that dates too much.

```html
<!DOCTYPE html>
<html lang="en">
<head>
<meta charset="utf-8">
<title>Quiet Harbour – Business Card</title>
<link rel="stylesheet" href="https://fonts.googleapis.com/css2?family=Open+Sans:wght@400;600;700&display=swap">
<style>
  :root {
    --backdrop: #022a3d;
    --card: #ffffff;
    --ink: #1e1e1e;
    --lavender: #a3a3d6;
    --violet: #6a6ac2;
  }
  html, body {
    margin: 0;
    padding: 0;
    width: 1200px;
    height: 900px;
    overflow: hidden;
    background: var(--backdrop);
  }
  .canvas {
    position: relative;
    width: 1200px;
    height: 900px;
    font-family: "Open Sans", Arial, sans-serif;
  }
  .business-card {
    position: absolute;
    left: 318px;
    top: 277px;
    width: 575px;
    height: 328px;
    background: var(--card);
    color: var(--ink);
  }
  .holder {
    position: absolute;
    left: 29px;
    top: 20px;
    margin: 0;
  }
  .holder-name {
    display: block;
    font-size: 21px;
    font-weight: 400;
    line-height: 30px;
  }
  .holder-role {
    display: block;
    font-size: 18px;
    line-height: 22px;
    color: var(--lavender);
  }
  .brand {
    position: absolute;
    right: 29px;
    top: 72px;
    text-align: right;
  }
  .brand-name {
    display: block;
    font-size: 31px;
    font-weight: 700;
    letter-spacing: 0.5px;
    line-height: 42px;
    color: var(--ink);
  }
  .brand-tagline {
    display: block;
    font-size: 15.5px;
    line-height: 20px;
    color: var(--violet);
  }
  .address {
    position: absolute;
    left: 29px;
    top: 143px;
    margin: 0;
    font-style: normal;
    font-size: 16px;
    line-height: 22px;
  }
  .contact {
    position: absolute;
    left: 29px;
    top: 260px;
    margin: 0;
    padding: 0;
    list-style: none;
    font-size: 16px;
    line-height: 22px;
  }
  .contact-label {
    font-weight: 700;
  }
</style>
</head>
<body>
<main class="canvas">
  <section class="business-card">
    <p class="holder">
      <span class="holder-name">Marta Holloway</span>
      <span class="holder-role">Director</span>
    </p>
    <div class="brand">
      <span class="brand-name">QUIET HARBOUR</span>
      <span class="brand-tagline">Tourism Marketing &amp; Representation</span>
    </div>
    <address class="address">
      Quiet Harbour Pty Ltd<br>
      Tourism Marketing &amp;<br>
      Representation<br>
      87 Wendover Parade Prahran,<br>
      Victoria, 3181 Australia
    </address>
    <ul class="contact">
      <li><span class="contact-label">T</span> +61 498203617</li>
      <li><span class="contact-label">E</span> marta@quietharbour-example.com.au</li>
    </ul>
  </section>
</main>
</body>
</html>
```